all sorted property services

Target Market(s)

General letter head for emails and letter quotes ect

Colors
0054AA
0677BA
7BADD7
CADEEF
E8F1F8
0094D4
00A9DD
6FCCEA
C7EBF8
E9F6FB

Requirements
Must have
• logo phone email website names
Nice to have
• what we do (from the website)

```html
<!DOCTYPE html>
<html lang="en">
<head>
<meta charset="utf-8">
<title>All Sorted Property Services — Letterhead</title>
<link rel="stylesheet" href="https://fonts.googleapis.com/css2?family=Poppins:wght@400;500;700&display=swap">
<style>
  :root {
    --navy: #1f2a7a;
    --brand-blue: #0054AA;
    --mid-blue: #0677BA;
    --sky: #0094D4;
    --bright: #00A9DD;
    --pale: #E8F1F8;
    --ink: #1a1a1a;
    --muted: #444;
    --backdrop: #cfcfcf;
    --paper: #ffffff;
  }
  * { box-sizing: border-box; margin: 0; padding: 0; }
  html, body { width: 1200px; height: 686px; overflow: hidden; }
  body {
    background: var(--backdrop);
    font-family: "Poppins", sans-serif;
    display: flex; align-items: center; justify-content: center;
  }
  .letterhead {
    position: relative;
    width: 500px; height: 646px;
    background: var(--paper);
    box-shadow: 0 6px 24px rgba(0,0,0,.18);
    overflow: hidden;
    color: var(--ink);
  }
  .letterhead__header {
    display: flex; justify-content: space-between; align-items: flex-start;
    padding: 34px 36px 0 36px;
  }
  .brand { display: flex; align-items: center; gap: 8px; }
  .brand__dot { width: 26px; height: 26px; border-radius: 50%; background: var(--brand-blue); }
  .brand__name {
    font-weight: 700; font-size: 12px; line-height: 1.15;
    color: var(--brand-blue); text-transform: uppercase; letter-spacing: .5px;
    max-width: 140px;
  }
  .contact { list-style: none; font-size: 8.5px; line-height: 1.55; text-align: right; color: var(--ink); }
  .contact li { display: flex; justify-content: flex-end; align-items: center; gap: 5px; }
  .contact svg { width: 9px; height: 9px; fill: var(--sky); flex: none; }
  .letter { padding: 42px 36px 0 36px; font-size: 8.5px; line-height: 1.55; color: var(--muted); }
  .letter__date { margin-bottom: 8px; }
  .recipient__name { font-weight: 700; font-size: 11px; color: var(--ink); }
  .recipient__role { margin-bottom: 4px; }
  .salutation { font-weight: 700; font-size: 12px; color: var(--ink); margin: 20px 0 10px; }
  .letter__body p { margin-bottom: 14px; max-width: 400px; }
  .signoff { margin-top: 14px; }
  .signoff__signature { width: 120px; height: 34px; background: var(--pale); border-radius: 3px; }
  .signoff__name { font-weight: 700; font-size: 16px; color: var(--ink); margin-top: 2px; }
  .signoff__role { font-size: 8.5px; }
  .footer-wave { position: absolute; left: 0; bottom: 0; width: 500px; height: 250px; }
</style>
</head>
<body>
<main class="letterhead">
  <header class="letterhead__header">
    <div class="brand">
      <span class="brand__dot"></span>
      <span class="brand__name">All Sorted Property Services</span>
    </div>
    <ul class="contact">
      <li>418 Maple Ridge Rd. Suite 12<br>Denton, TX 76201 <svg viewBox="0 0 10 10"><path d="M5 0a3.5 3.5 0 0 0-3.5 3.5C1.5 6 5 10 5 10s3.5-4 3.5-6.5A3.5 3.5 0 0 0 5 0zm0 5a1.5 1.5 0 1 1 0-3 1.5 1.5 0 0 1 0 3z"/></svg></li>
      <li>(555) 214-7730 <svg viewBox="0 0 10 10"><path d="M2 0l2 2.5-1 1.2a6 6 0 0 0 3.3 3.3l1.2-1L10 8l-1.5 2C4 10 0 6 0 1.5z"/></svg></li>
      <li>www.allsortedps.com <svg viewBox="0 0 10 10"><circle cx="5" cy="5" r="4.5" fill="none" stroke="#0094D4" stroke-width="1"/><path d="M.5 5h9M5 .5c-2 2.5-2 6.5 0 9M5 .5c2 2.5 2 6.5 0 9" fill="none" stroke="#0094D4" stroke-width=".8"/></svg></li>
      <li>hello@allsortedps.com <svg viewBox="0 0 10 10"><path d="M0 2h10v6H0z"/><path d="M0 2l5 3.5L10 2" fill="none" stroke="#fff" stroke-width=".8"/></svg></li>
    </ul>
  </header>

  <section class="letter">
    <p class="letter__date">August-05-2019</p>
    <div class="recipient">
      <p class="recipient__name">Helena Brandt</p>
      <p class="recipient__role">Director</p>
      <p>418 Maple Ridge Rd. Suite 12<br>Denton, TX 76201</p>
    </div>
    <p class="salutation">Helena Brandt</p>
    <div class="letter__body">
      <p>Lorem ipsum dolor sit amet, consectetuer adipiscing elit, sed diam nonummy nibh euismod tincidunt ut laoreet dolore magna aliquam erat volutpat. Ut wisi enim ad minim veniam, quis nostrud exerci tation ullamcorper suscipit lobortis.</p>
      <p>Lorem ipsum dolor sit amet, cons ectetuer adipiscing elit, sed diam nonummy nibh euismod tincidunt ut laoreet dolore magna aliquam erat volutpat. Ut wisi enim ad minim veniam, quis nostrud exerci tation ullamcorper suscipit lobortis nisl ut aliquip ex ea commodo consequat. Lorem ipsum dolor sit amet, consectetuer volutpat. Ut wisi enim ad minim veniam, quis nostrud exerci tation ullamcorper suscipit lobortis nisl ut aliquip ex ea commodo consequat. Duis autem</p>
      <p>vel eum iriure dolor in hendrerit in vulputate velit esse molestie consequat, vel illum dolore eu feugiat nulla facilisis at vero eros et accumsan et iusto odio dignissim qui blandit praesent luptatum zzril delenit augue duis dolore te feugait nulla facilisi. Lorem ipsum dolor sit amet, cons ectetuer adipiscing elit, sed diam nonummy nibh euismod tincidunt ut laoreet dolore magna aliquam erat volutpat. Ut wisi enim.</p>
    </div>
    <div class="signoff">
      <div class="signoff__signature" role="img" aria-label="Handwritten signature"></div>
      <p class="signoff__name">Owen Hartley</p>
      <p class="signoff__role">Co-Founder</p>
    </div>
  </section>

  <svg class="footer-wave" viewBox="0 0 500 250" preserveAspectRatio="none" aria-hidden="true">
    <defs>
      <linearGradient id="waveFill" x1="0" y1="1" x2="1" y2="0">
        <stop offset="0" stop-color="var(--navy)"/>
        <stop offset=".6" stop-color="#0054AA"/>
        <stop offset="1" stop-color="#0677BA"/>
      </linearGradient>
    </defs>
    <path d="M0 250 L0 236 C150 236 300 220 370 160 C420 115 460 40 500 10 L500 250 Z" fill="url(#waveFill)"/>
    <path d="M0 232 C150 232 290 216 360 156 C410 112 455 35 500 4" fill="none" stroke="#fff" stroke-width="3"/>
    <path d="M0 227 C150 227 285 211 355 151 C405 108 450 30 500 0" fill="none" stroke="#00A9DD" stroke-width="3"/>
  </svg>
</main>
</body>
</html>
```